Cover for CD-single

MAVE is a young singer-songwriter and needs a CD cover design for her first single "Paper boats at dawn". Her song is about her best friend who recently moved from Europe to Australia with her family. But even though they now live on the other side of the world, they will always be there for each other.
You can use the picture attached or you can see it as an inspiration.
Please put the name of the artist: MAVE
and the name of the song on the cover: Paper boats at dawn

```html
<!DOCTYPE html>
<html lang="en">
<head>
<meta charset="utf-8">
<title>Paper boats at dawn – MAVE</title>
<link href="https://fonts.googleapis.com/css2?family=DM+Serif+Display&family=Montserrat:wght@400&family=Caveat:wght@500&display=swap" rel="stylesheet">
<style>
  :root {
    --sky-top: #c9bcd6;
    --sky-pink: #dcc6d8;
    --hills: #7d8aa0;
    --town: #a7a3b4;
    --ground: #918892;
    --bench-red: #d9553f;
    --text-white: #ffffff;
    --script-cream: #fbeee6;
  }
  html, body {
    margin: 0;
    padding: 0;
    width: 1200px;
    height: 1200px;
    overflow: hidden;
    background: var(--sky-top);
  }
  .cover {
    position: relative;
    width: 1200px;
    height: 1200px;
    overflow: hidden;
  }
  .cover-photo {
    position: absolute;
    inset: 0;
    background:
      radial-gradient(ellipse 460px 130px at 575px 805px, var(--bench-red) 0%, rgba(217, 85, 63, 0.85) 45%, rgba(217, 85, 63, 0) 100%),
      linear-gradient(
        180deg,
        var(--sky-top) 0%,
        var(--sky-pink) 26%,
        var(--hills) 36%,
        var(--town) 55%,
        var(--ground) 78%,
        #a39aa0 100%
      );
  }
  .song-title {
    position: absolute;
    top: 128px;
    left: 0;
    width: 1200px;
    margin: 0;
    text-align: center;
    font-family: "DM Serif Display", Georgia, serif;
    font-weight: 400;
    font-size: 96px;
    line-height: 1;
    letter-spacing: -2px;
    color: var(--text-white);
  }
  .artist-name {
    position: absolute;
    top: 256px;
    right: 107px;
    margin: 0;
    font-family: "Montserrat", Arial, sans-serif;
    font-weight: 400;
    font-size: 28px;
    letter-spacing: 4px;
    color: var(--text-white);
  }
  .tagline {
    position: absolute;
    top: 770px;
    left: 432px;
    margin: 0;
    font-family: "Caveat", cursive;
    font-weight: 500;
    font-size: 36px;
    line-height: 1;
    letter-spacing: 1px;
    color: var(--script-cream);
    transform: rotate(6deg);
    transform-origin: left center;
  }
</style>
</head>
<body>
  <main class="cover">
    <div class="cover-photo" role="img" aria-label="Photo: two friends hugging on a red bench at a lookout above a lakeside town, with hills and snowy mountains under a lavender dusk sky"></div>
    <h1 class="song-title">Paper boats at dawn</h1>
    <p class="artist-name">MAVE</p>
    <p class="tagline">for each other</p>
  </main>
</body>
</html>
```